Etiketten für Charity Bier gesucht
Zielgruppe
Wir engagieren uns ehrenamtlich für Kinder in Afrika.
In Einsatz-Teams von freiwilligen Helfern, sammeln wir während 8 Monaten Spendengelder, um Kindern in Townships's Südafrikas eine Zukunft zu bauen, in dem wir nicht staatliche Kindertagesstätten engagierter einheimischer Frauen umbauen.
Vorher bestehen die KITA's nur aus rostigen Wellblechhütten, welche nicht isoliert sind und auf dem KITA Gelände befindet sich weder Rasen, noch ein Spielplatz.
Aufgabenstellung
Um Spenden zu sammeln, möchten wir ein Charity Bier auf den Markt bringen.
Infos zu den Maßen der Etiketten: Sie sollten nicht breiter als 8 cm sein. Wichtig ist, dass sich in der Ecke links oben keine Angaben befinden, da die obere linke Kante schräg nach oben verlaufen wird. Welche Angaben müssen zwingend auf den Etiketten zu finden sein?
Die Promill-Angaben (5.2% VOL)
Inhalts-Angabe (33cl) das Logo des Bierherstellers sollte auch mit auf die Etikette (nicht all zu gross) (siehe Bild Nr.2)
Die Info's zum Bier (Biersorte: Tannfelsbräu ORIGINAL)
Der Name des Bier's sollte Charity Bier sein.
Wir möchten auf der Etikette auch folgendes unbedingt vermerken:
'Diese Flache (Bier) füllt 10 Breischalen für Kinder in Afrika'
Ansonsten haben wir überhaupt keine Vorstellung, was wir wörtlich noch auf die Etikette packen möchten (vielleicht fällt euch ja noch was tolles ein:-)
Was wir uns vom Design her so vorstellen:
Ich habe noch 3 Bilder (siehe Bild 3-4) dazugefügt, mit Designs, welche mir auf Anhieb sehr sehr gut gefallen (damit ihr einen Anhaltspunkt habt:-) Aber ich lasse mich auch gerne von anderen Design-Formen überraschen.

```html
<!DOCTYPE html>
<html lang="de">
<head>
<meta charset="utf-8">
<title>Charity Bier – Etiketten</title>
<link rel="stylesheet" href="https://fonts.googleapis.com/css2?family=Archivo+Black&family=Oswald:wght@300;400;500&family=Open+Sans:wght@400&display=swap">
<style>
  :root {
    --paper: #ffffff;
    --gold: #f1b400;
    --berry: #8e1f5e;
    --olive: #858633;
    --cocoa: #3c2b30;
    --signal-red: #d42127;
    --amber: #e08a1a;
    --blush: #e6bcd3;
    --lilac: #d8c6df;
  }
  html, body {
    margin: 0;
    padding: 0;
    overflow: hidden;
    background: var(--paper);
  }
  .canvas {
    position: relative;
    width: 1200px;
    height: 450px;
    overflow: hidden;
    background: var(--paper);
  }
  .label {
    position: absolute;
    top: 54px;
    width: 359px;
    height: 359px;
  }
  .label--gold  { left: 28px;  --panel: var(--gold);  --charity: var(--signal-red); --claim-1: var(--signal-red); --claim-2: var(--cocoa); --claim-3: var(--paper); --story: var(--paper); --accent: var(--paper); --brand: var(--amber); }
  .label--berry { left: 421px; --panel: var(--berry); --charity: var(--paper); --claim-1: var(--cocoa); --claim-2: var(--paper); --claim-3: var(--blush); --story: var(--cocoa); --accent: var(--gold); --brand: var(--gold); }
  .label--olive { left: 813px; --panel: var(--olive); --charity: var(--paper); --claim-1: var(--cocoa); --claim-2: var(--paper); --claim-3: var(--lilac); --story: var(--cocoa); --accent: var(--gold); --brand: var(--gold); }

  .label__art {
    position: absolute;
    inset: 0;
    width: 359px;
    height: 359px;
    overflow: visible;
    filter: drop-shadow(3px 5px 5px rgba(0, 0, 0, 0.45));
  }
  .label__sheet { fill: var(--paper); }
  .label__panel { fill: var(--panel); }
  .label__band  { fill: var(--cocoa); }
  .label__illustration { fill: rgba(255, 255, 255, 0.22); }

  .label__brand {
    font-family: "Oswald", sans-serif;
    font-weight: 500;
    font-size: 15px;
    fill: var(--brand);
  }
  .label__headline {
    font-family: "Archivo Black", sans-serif;
  }
  .label__headline--charity { fill: var(--charity); font-size: 76px; }
  .label__headline--bier    { fill: var(--cocoa);  font-size: 90px; }

  .label__claim {
    font-family: "Oswald", sans-serif;
    font-weight: 400;
    font-size: 21px;
  }
  .label__claim--1 { fill: var(--claim-1); }
  .label__claim--2 { fill: var(--claim-2); }
  .label__claim--3 { fill: var(--claim-3); }

  .label__variety {
    font-family: "Open Sans", sans-serif;
    font-size: 16px;
    fill: var(--accent);
  }
  .label__volume {
    font-family: "Oswald", sans-serif;
    font-weight: 400;
    fill: var(--accent);
  }
  .label__volume-small { font-size: 11px; }

  .label__story {
    position: absolute;
    left: 8px;
    top: 245px;
    width: 177px;
    margin: 0;
    font-family: "Oswald", sans-serif;
    font-weight: 300;
    font-size: 10px;
    line-height: 12.2px;
    text-align: justify;
    hyphens: manual;
    color: var(--story);
  }
</style>
</head>
<body>
<main class="canvas">

  <article class="label label--gold">
    <svg class="label__art" viewBox="0 0 359 359" aria-hidden="false">
      <polygon class="label__sheet" points="0,0 359,0 359,359 0,359"/>
      <polygon class="label__panel" points="0,70 359,0 359,359 0,359"/>
      <polygon class="label__band" points="0,333 359,288 359,359 0,359"/>
      <text class="label__brand" x="134" y="62">Tannfelsbräu</text>
      <text class="label__headline label__headline--charity" x="0" y="147" textLength="359" lengthAdjust="spacingAndGlyphs">CHARITY</text>
      <text class="label__headline label__headline--bier" x="0" y="219" textLength="169" lengthAdjust="spacingAndGlyphs">BIER</text>
      <text class="label__claim label__claim--1" x="193" y="182" textLength="154" lengthAdjust="spacingAndGlyphs">Diese Flasche Bier</text>
      <text class="label__claim label__claim--2" x="193" y="203" textLength="150" lengthAdjust="spacingAndGlyphs">füllt 10 Breischalen</text>
      <text class="label__claim label__claim--3" x="193" y="224" textLength="154" lengthAdjust="spacingAndGlyphs">für Kinder in Afrika</text>
      <g role="img" aria-label="Illustration: Kind neben einer Schale Brei">
        <rect class="label__illustration" x="208" y="234" width="130" height="103" rx="10"/>
      </g>
      <text class="label__variety" x="149" y="353">ORIGINAL</text>
      <text class="label__volume" x="349" y="339" text-anchor="end" font-size="17">33<tspan class="label__volume-small">cl</tspan></text>
      <text class="label__volume" x="349" y="355" text-anchor="end" font-size="17">5.2 <tspan class="label__volume-small">% VOL</tspan></text>
    </svg>
    <p class="label__story">Das Rezept hat sich im Verlauf der mehrjährigen Geschichte stets weiterent&shy;wickelt zu diesem mittlerweile unverkennbar feinen Geschmack. Aus verschiedenen Malzsorten, feinstem Schweizer Hopfen und Tannfels-Wasser</p>
  </article>

  <article class="label label--berry">
    <svg class="label__art" viewBox="0 0 359 359">
      <polygon class="label__sheet" points="0,64 359,0 359,359 0,359"/>
      <polygon class="label__panel" points="0,72 359,7 359,359 0,359"/>
      <polygon class="label__band" points="0,333 359,288 359,359 0,359"/>
      <text class="label__brand" x="134" y="64">Tannfelsbräu</text>
      <text class="label__headline label__headline--charity" x="0" y="149" textLength="359" lengthAdjust="spacingAndGlyphs">CHARITY</text>
      <text class="label__headline label__headline--bier" x="0" y="221" textLength="169" lengthAdjust="spacingAndGlyphs">BIER</text>
      <text class="label__claim label__claim--1" x="193" y="184" textLength="154" lengthAdjust="spacingAndGlyphs">Diese Flasche Bier</text>
      <text class="label__claim label__claim--2" x="193" y="205" textLength="150" lengthAdjust="spacingAndGlyphs">füllt 10 Breischalen</text>
      <text class="label__claim label__claim--3" x="193" y="226" textLength="154" lengthAdjust="spacingAndGlyphs">für Kinder in Afrika</text>
      <g role="img" aria-label="Illustration: Kind neben einer Schale Brei">
        <rect class="label__illustration" x="208" y="236" width="130" height="103" rx="10"/>
      </g>
      <text class="label__variety" x="149" y="353">ORIGINAL</text>
      <text class="label__volume" x="349" y="339" text-anchor="end" font-size="17">33<tspan class="label__volume-small">cl</tspan></text>
      <text class="label__volume" x="349" y="355" text-anchor="end" font-size="17">5.2 <tspan class="label__volume-small">% VOL</tspan></text>
    </svg>
    <p class="label__story">Das Rezept hat sich im Verlauf der mehrjährigen Geschichte stets weiterent&shy;wickelt zu diesem mittlerweile unverkennbar feinen Geschmack. Aus verschiedenen Malzsorten, feinstem Schweizer Hopfen und Tannfels-Wasser</p>
  </article>

  <article class="label label--olive">
    <svg class="label__art" viewBox="0 0 359 359">
      <polygon class="label__sheet" points="0,64 359,0 359,359 0,359"/>
      <polygon class="label__panel" points="0,72 359,7 359,359 0,359"/>
      <polygon class="label__band" points="0,333 359,288 359,359 0,359"/>
      <text class="label__brand" x="134" y="64">Tannfelsbräu</text>
      <text class="label__headline label__headline--charity" x="0" y="149" textLength="359" lengthAdjust="spacingAndGlyphs">CHARITY</text>
      <text class="label__headline label__headline--bier" x="0" y="221" textLength="169" lengthAdjust="spacingAndGlyphs">BIER</text>
      <text class="label__claim label__claim--1" x="193" y="184" textLength="154" lengthAdjust="spacingAndGlyphs">Diese Flasche Bier</text>
      <text class="label__claim label__claim--2" x="193" y="205" textLength="150" lengthAdjust="spacingAndGlyphs">füllt 10 Breischalen</text>
      <text class="label__claim label__claim--3" x="193" y="226" textLength="154" lengthAdjust="spacingAndGlyphs">für Kinder in Afrika</text>
      <g role="img" aria-label="Illustration: Kind neben einer Schale Brei">
        <rect class="label__illustration" x="208" y="236" width="130" height="103" rx="10"/>
      </g>
      <text class="label__variety" x="149" y="353">ORIGINAL</text>
      <text class="label__volume" x="349" y="339" text-anchor="end" font-size="17">33<tspan class="label__volume-small">cl</tspan></text>
      <text class="label__volume" x="349" y="355" text-anchor="end" font-size="17">5.2 <tspan class="label__volume-small">% VOL</tspan></text>
    </svg>
    <p class="label__story">Das Rezept hat sich im Verlauf der mehrjährigen Geschichte stets weiterent&shy;wickelt zu diesem mittlerweile unverkennbar feinen Geschmack. Aus verschiedenen Malzsorten, feinstem Schweizer Hopfen und Tannfels-Wasser</p>
  </article>

</main>
</body>
</html>
```